Elite Company Card

create a new dark colored, with metallic accents business card that people will not want to throw away

prefer rounded corners

Font styles to use
Serif

Requirements
Must have
• metallic accents
Nice to have
• 2 sided, the company logo prominent on one side the person and company info on the other side
Should not have
• no white

```html
<!DOCTYPE html>
<html lang="en">
<head>
<meta charset="utf-8">
<title>Summit Collision &amp; Refinish — Business Card</title>
<link rel="stylesheet" href="https://fonts.googleapis.com/css2?family=Mulish:wght@500;600;700&display=swap">
<style>
  :root {
    --backdrop: #000000;
    --navy: #1e3a6b;
    --navy-deep: #1a3160;
    --silver-light: #f2f2f3;
    --silver-mid: #dcdcde;
    --silver-dark: #b9babd;
    --rule-light: #c9ccd2;
  }
  * { margin: 0; padding: 0; box-sizing: border-box; }
  html, body { width: 1200px; height: 1000px; overflow: hidden; background: var(--backdrop); }
  body { position: relative; font-family: "Mulish", sans-serif; color: var(--navy); }

  .card {
    position: absolute;
    left: 262px;
    width: 675px;
    height: 384px;
    border-radius: 40px;
    overflow: hidden;
    background: var(--navy);
  }
  .card--front { top: 97px; }
  .card--back { top: 519px; }

  .metal {
    position: absolute;
    left: 0; right: 0;
    background: linear-gradient(100deg, var(--silver-dark) 0%, var(--silver-light) 30%, var(--silver-mid) 55%, var(--silver-light) 75%, var(--silver-dark) 100%);
  }
  .rule { position: absolute; left: 0; right: 0; height: 4px; }
  .rule--silver { background: var(--rule-light); }
  .rule--navy { background: var(--navy-deep); }

  /* front */
  .card--front .metal { top: 104px; height: 176px; }
  .brand-front {
    position: absolute;
    left: 0; right: 0; top: 150px;
    text-align: center;
    font-weight: 700;
    font-size: 30px;
    line-height: 1.2;
    color: var(--navy);
  }

  /* back */
  .card--back .metal { top: 29px; height: 328px; }
  .divider { position: absolute; left: 333px; top: 64px; width: 4px; height: 262px; }

  .info-left {
    position: absolute;
    left: 60px; width: 220px; top: 88px;
    text-align: center;
  }
  .brand-back {
    font-weight: 700;
    font-size: 21px;
    line-height: 1.25;
    color: var(--navy);
    margin-bottom: 28px;
  }
  .hours { font-size: 17px; line-height: 24px; font-weight: 500; }
  .hours dt { font-weight: 700; }
  .hours dd + dt { margin-top: 12px; }

  .info-right { position: absolute; left: 405px; top: 78px; }
  .person-name { font-size: 26px; font-weight: 600; line-height: 30px; }
  .person-role { font-size: 16px; font-weight: 500; line-height: 18px; margin-bottom: 24px; }
  .location { font-style: normal; font-size: 17px; line-height: 24px; font-weight: 500; }
  .location + .location { margin-top: 19px; }
</style>
</head>
<body>

<section class="card card--front" aria-label="Card front">
  <div class="rule rule--silver" style="top:96px"></div>
  <div class="rule rule--navy" style="top:100px"></div>
  <div class="metal"></div>
  <div class="rule rule--navy" style="top:280px"></div>
  <div class="rule rule--silver" style="top:284px"></div>
  <p class="brand-front">Summit Collision<br>&amp; Refinish</p>
</section>

<section class="card card--back" aria-label="Card back">
  <div class="rule rule--silver" style="top:21px"></div>
  <div class="rule rule--navy" style="top:25px"></div>
  <div class="metal"></div>
  <div class="rule rule--navy" style="top:357px"></div>
  <div class="rule rule--silver" style="top:361px"></div>

  <svg class="divider" viewBox="0 0 4 262" preserveAspectRatio="none" aria-hidden="true">
    <path d="M2 0 L4 131 L2 262 L0 131 Z" fill="#1e3a6b"/>
  </svg>

  <div class="info-left">
    <p class="brand-back">Summit Collision<br>&amp; Refinish</p>
    <dl class="hours">
      <dt>Monday - Friday</dt>
      <dd>7:30 AM - 5:00 PM</dd>
      <dt>Saturday &amp; Sunday</dt>
      <dd>Closed</dd>
    </dl>
  </div>

  <div class="info-right">
    <p class="person-name">Daniel Reyes</p>
    <p class="person-role">Owner</p>
    <address class="location">2714 Alder Ct.<br>Maple Falls, IL 62790<br>(217) 555-0142</address>
    <address class="location">1650 N. Ridgeway Blvd.<br>Maple Falls, IL 62795<br>(217) 555-0187</address>
  </div>
</section>

</body>
</html>
```